IT supplier clean wordpress website - payment guaranteed

Clean website design for a wordpress based website
Design only - PSD delivery with images

current website: www.quorvel.net
please use your imagination and try something out of the box...
We like https://tavrinex.com.au as look and feel, but you don't have to copy it, you can be creative

We like the navigation header and the phone number, but do not need 'instant quote' so the 1300 phone number and the 'lock' icon for login can be on the same line

Site Map:
IT support
VoIP
Internet and Data
Cloud hosting
About
Contact

Our logo is attached, it can be used light or dark.
Our only color used is the warm grey Pantone 8003C hex #877A69

You will only need to design the homepage to win the competition, but the winning designer will be required to supply without extra charges:
1. Home page design
2. A second, standard page template design
3. An icon set in colors appropriate to the site that have icons to match the subjects in these pages:
https://tavrinex.com.au/products/
https://tavrinex.com.au/making-the-switch/
https://tavrinex.com.au/why-tavrinex/
We will create a single page version of the options on https://tavrinex.com.au/solutions/
4.Any images used

Please avoid stock photos that are too common - e.g. smiling woman with headset, try to make the design stand out with simple images and well-designed layout.

Target Market(s)

Mid-size business clients

Industry/Entity Type

It Company

Number of Pages Required

1 page

Requirements
Must have
• Quor logo
• Use Quor color

```html
<!DOCTYPE html>
<html lang="en">
<head>
<meta charset="utf-8">
<title>Quor — IT Outsourcing</title>
<link href="https://fonts.googleapis.com/css2?family=Roboto:wght@300;400;500;700&display=swap" rel="stylesheet">
<style>
:root{
  --brand:#877a69;
  --brand-dark:#6f6456;
  --ink:#333;
  --muted:#666;
  --line:#d9d9d9;
  --pale:#f8f8f8;
  --white:#fff;
  --footer-ink:#f1ece6;
}
*{box-sizing:border-box;margin:0;padding:0}
html,body{width:1200px;height:2908px;overflow:hidden}
body{font-family:'Roboto',Arial,sans-serif;color:var(--ink);background:var(--white);position:relative}
.abs{position:absolute}
.center{text-align:center;left:0;width:1200px}

/* header */
.site-header{position:absolute;top:0;left:0;width:1200px;height:160px;background:var(--white)}
.brand{position:absolute;left:100px;top:52px;display:flex;align-items:center;gap:14px}
.brand i{display:block;width:26px;height:26px;background:var(--brand)}
.brand span{font-size:44px;font-weight:300;line-height:1;color:var(--brand)}
.login{position:absolute;left:876px;top:42px;font-size:14px;font-weight:500;display:flex;align-items:center;gap:5px}
.phone{position:absolute;left:960px;top:32px;font-size:26px;padding-bottom:4px;border-bottom:2px solid var(--ink)}
.main-nav{position:absolute;top:100px;right:99px;display:flex;gap:42px;font-size:14px}

/* hero */
.hero{position:absolute;top:160px;left:0;width:1200px;height:570px;
  background:linear-gradient(100deg,#4a4743 0%,#6e6b67 30%,#8c8a86 55%,#5f5c58 80%,#3f3d3a 100%)}
.hero-curve{position:absolute;top:640px;left:0}
.hero-title{top:380px;font-size:90px;font-weight:700;color:var(--white)}
.hero-sub{top:490px;font-size:17px;color:var(--white)}
.dots{position:absolute;top:618px;left:572px;display:flex;gap:4px}
.dots i{width:18px;height:18px;border-radius:50%;border:2px solid var(--white);display:block}
.dots i.on{background:var(--white)}

/* section titles */
.section-title{font-size:44px;font-weight:300;color:#333}
.section-title em{font-style:normal;color:var(--brand)}

/* welcome */
.welcome-title{top:740px}
.welcome-text{top:800px;left:190px;width:820px;text-align:center;font-size:16px;line-height:30px;color:var(--muted)}
.rule{top:892px;left:218px;width:764px;height:1px;background:#ececec}
.service{position:absolute;top:934px;width:300px;text-align:center}
.service .badge{width:148px;height:148px;border-radius:50%;background:var(--brand);margin:0 auto;border:4px solid #a99e91;display:flex;align-items:center;justify-content:center}
.service h3{margin-top:20px;font-size:23px;font-weight:400;color:#222}
.service p{margin-top:8px;font-size:14px;line-height:24px;color:var(--muted)}
.btn{display:inline-block;border:2px solid #bdb6ad;color:var(--brand-dark);font-size:17px;padding:11px 26px;background:var(--white)}
.service .btn{margin-top:22px;width:154px;padding:11px 0}

/* about */
.about{position:absolute;top:1318px;left:0;width:1200px;height:440px;
  background:linear-gradient(90deg,#8f8b86 0%,#b5b1ab 35%,#a7a39d 60%,#7d7973 100%)}
.about-title{top:1375px;font-size:46px;font-weight:300;color:var(--white)}
.about-text{top:1450px;left:180px;width:840px;text-align:center;font-size:18px;line-height:30px;color:var(--white)}
.about-text p+p{margin-top:20px}
.btn-ghost{position:absolute;top:1620px;left:452px;width:296px;height:50px;border:2px solid #e6e2dc;color:var(--white);font-size:15px;font-weight:500;display:flex;align-items:center;justify-content:center}

/* video */
.video-section{position:absolute;top:1758px;left:0;width:1200px;height:504px;background:var(--pale)}
.video-title{top:1808px}
.video-copy{top:1918px;left:100px;width:510px;font-size:14px;line-height:27px;color:#555}
.video-copy p+p{margin-top:16px}
.more{position:absolute;top:2142px;left:100px;width:234px;height:48px;border:2px solid #c4beb6;font-size:16px;color:var(--brand-dark);display:flex;align-items:center;justify-content:center;gap:10px;background:var(--white)}
.video-frame{position:absolute;top:1908px;left:668px;width:436px;height:282px;border:2px solid #ddd;background:var(--white);padding:9px}
.video-still{width:100%;height:100%;background:linear-gradient(110deg,#2e2f33 0%,#6a6d73 40%,#c9cbce 65%,#9aa0a7 100%);display:flex;align-items:center;justify-content:center}

/* partners */
.partners-title{top:2310px}
.partner-row{position:absolute;top:2402px;left:100px;display:flex;gap:14px}
.partner{width:155px;height:94px;border:1px solid var(--line);display:flex;align-items:center;justify-content:center;background:var(--white)}
.partner i{display:block;width:100px;height:26px;background:#e2e2e2;border-radius:3px}
.arrow{position:absolute;top:2432px}

/* footer */
.site-footer{position:absolute;top:2570px;left:0;width:1200px;height:338px;background:var(--brand);color:var(--footer-ink)}
.fcol{position:absolute;top:42px}
.fcol h4{font-size:14px;font-weight:500;color:var(--white);margin-bottom:18px}
.fcol li{list-style:none;font-size:11px;line-height:28px}
.fcol p{font-size:12px;line-height:22px}
.subscribe-input{margin-top:22px;width:244px;height:40px;background:var(--white);color:#999;font-size:11px;padding:13px 14px}
.subscribe-btn{margin-top:16px;width:90px;height:40px;background:#222;color:var(--white);font-size:12px;display:flex;align-items:center;justify-content:center}
.contact-line{display:flex;align-items:center;gap:10px;font-size:11px;margin-top:10px}
.footer-bar{position:absolute;top:266px;left:0;width:1200px;height:1px;background:rgba(255,255,255,.25)}
.copyright{position:absolute;top:294px;left:100px;font-size:11px}
.social{position:absolute;top:292px;left:776px;display:flex;align-items:center;gap:22px;font-size:11px}
.social i{display:block;width:12px;height:12px;border-radius:50%;background:var(--footer-ink)}
</style>
</head>
<body>

<header class="site-header">
  <div class="brand"><i></i><span>Quor</span></div>
  <div class="login">
    <svg width="10" height="12" viewBox="0 0 10 12"><rect x="0" y="5" width="10" height="7" fill="#333"/><path d="M2 5V3.5a3 3 0 016 0V5" stroke="#333" stroke-width="1.5" fill="none"/></svg>
    LOGIN
  </div>
  <div class="phone">1300 482 913</div>
  <nav class="main-nav">
    <span>Home</span><span>IT Support</span><span>VoIP</span><span>Internet And Data</span><span>Cloud Hosting</span><span>About</span><span>Contact</span>
  </nav>
</header>

<section class="hero" role="img" aria-label="Photo of IT staff working at desks with computer monitors in an office"></section>
<svg class="hero-curve" width="1200" height="92" viewBox="0 0 1200 92"><path d="M0 92V66Q600 -40 1200 66V92Z" fill="#fff"/></svg>
<h1 class="abs center hero-title">IT Outsourcing</h1>
<p class="abs center hero-sub">We support the open exchange of ideas in the IT community and put a lot in ourselves.</p>
<div class="dots"><i></i><i class="on"></i><i class="on"></i></div>

<h2 class="abs center section-title welcome-title">Welcome to <em>Quor</em></h2>
<p class="abs welcome-text">We pride ourselves in our skill, integrity and ability to think and act in your best interests - that's what gets us customer referrals time after time.</p>
<div class="abs rule"></div>

<div class="service" style="left:90px">
  <div class="badge"><svg width="70" height="84" viewBox="0 0 70 84" fill="none" stroke="#fff" stroke-width="6" stroke-linecap="round"><rect x="22" y="3" width="26" height="48" rx="13" fill="#fff"/><path d="M8 38a27 27 0 0054 0M35 66v14"/></svg></div>
  <h3>DATA AND VOICE</h3>
  <p>Quor supplies a wide range of business<br>data connections which are reliable..</p>
  <span class="btn">READ MORE</span>
</div>
<div class="service" style="left:450px">
  <div class="badge"><svg width="92" height="56" viewBox="0 0 92 56"><path d="M20 54a17 17 0 01-2-34 24 24 0 0146-4 19 19 0 018 38z" fill="#fff"/></svg></div>
  <h3>CLOUD SERVICES</h3>
  <p>Quor provides a range of cloud services,<br>including Software as a service..</p>
  <span class="btn">READ MORE</span>
</div>
<div class="service" style="left:820px">
  <div class="badge"><svg width="84" height="84" viewBox="0 0 84 84" fill="none" stroke="#fff" stroke-width="6" stroke-linecap="round"><path d="M12 48V38a30 30 0 0160 0v10"/><rect x="6" y="40" width="16" height="26" rx="6" fill="#fff"/><rect x="62" y="40" width="16" height="26" rx="6" fill="#fff"/><path d="M70 66q0 12-22 12"/></svg></div>
  <h3>SUPPORT</h3>
  <p>A wide range of skills and certifications<br>with a great bedside manner..</p>
  <span class="btn">READ MORE</span>
</div>

<section class="about" role="img" aria-label="Faded photo of people standing in a bright open office"></section>
<h2 class="abs center about-title">About Quor</h2>
<div class="abs about-text">
  <p>Servicing industry's IT needs with experience in extensive technologies and platforms with a focus on customer service.</p>
  <p>From consultancy and planning to software, hardware, telephony, connectivity and cabling to ISP services, databases and business to business transactions - a true end-to-end solution.</p>
</div>
<span class="btn-ghost">LEAD GENERATION OPPORTUNITIES</span>

<section class="video-section"></section>
<h2 class="abs center section-title video-title">Our <em>Video</em></h2>
<div class="abs video-copy">
  <p>From consultancy and planning to software, hardware, telephony, connectivity and cabling to ISP services, databases and business to business transactions - a true end-to-end solution.</p>
  <p>We collect aggregate information on what pages users or visit and information volunteered by the users such as specific requests to be added to our mailing list. We never give out this information to other companies, and any details given to us are treated in confidence. You will not end up on someone else's mailing list.</p>
</div>
<span class="more">MORE INFORMATION <svg width="8" height="12" viewBox="0 0 8 12"><path d="M1 1l5 5-5 5" stroke="#6f6456" stroke-width="2" fill="none"/></svg></span>
<div class="video-frame">
  <div class="video-still" role="img" aria-label="Video still of hands working on server hardware in a rack">
    <svg width="72" height="72" viewBox="0 0 72 72"><circle cx="36" cy="36" r="33" fill="none" stroke="#fff" stroke-width="4"/><path d="M28 22l22 14-22 14z" fill="#fff"/></svg>
  </div>
</div>

<h2 class="abs center section-title partners-title">Our <em>Partners</em></h2>
<svg class="arrow" style="left:58px" width="18" height="30" viewBox="0 0 18 30"><path d="M15 2L3 15l12 13" stroke="#ccc" stroke-width="3" fill="none"/></svg>
<div class="partner-row">
  <div class="partner"><i></i></div><div class="partner"><i></i></div><div class="partner"><i></i></div>
  <div class="partner"><i></i></div><div class="partner"><i></i></div><div class="partner"><i></i></div>
</div>
<svg class="arrow" style="left:1128px" width="18" height="30" viewBox="0 0 18 30"><path d="M3 2l12 13L3 28" stroke="#ccc" stroke-width="3" fill="none"/></svg>

<footer class="site-footer">
  <div class="fcol" style="left:100px">
    <h4>LINKS</h4>
    <ul><li>Home</li><li>IT Support</li><li>VoIP</li><li>Internet And Data</li><li>Cloud Hosting</li><li>About</li></ul>
  </div>
  <div class="fcol" style="left:253px">
    <h4>JOIN OUR NEWSLETTER</h4>
    <p>Excepteur sint occaecat cupidatat non proident,<br>sunt in culpa qui</p>
    <div class="subscribe-input">Enter Your Email</div>
    <div class="subscribe-btn">SUBSCRIBE</div>
  </div>
  <div class="fcol" style="left:590px">
    <h4>INFORMATION</h4>
    <ul><li>Terms &amp; Conditions</li><li>Privacy policy</li><li>Disclaimer</li><li>Contact us</li><li>Sitemap</li></ul>
  </div>
  <div class="fcol" style="left:787px">
    <h4>WHY US</h4>
    <ul><li>Customers</li><li>Team</li><li>FAQ</li><li>News</li><li>Others</li></ul>
  </div>
  <div class="fcol" style="left:955px">
    <h4>CONTACT INFO</h4>
    <p style="font-size:13px">Quor</p>
    <p style="font-size:11px;line-height:20px;margin-top:6px">Suite 7, 14-18 Larkfield Rd,<br>Brenmoor NSW 2094</p>
    <div class="contact-line"><svg width="11" height="11" viewBox="0 0 24 24"><path d="M6 2l4 5-2 3a12 12 0 006 6l3-2 5 4-3 4C11 22 2 13 2 5z" fill="#f1ece6"/></svg>+61 (2) 70418836</div>
    <div class="contact-line"><svg width="12" height="10" viewBox="0 0 24 18"><rect width="24" height="18" fill="#f1ece6"/><path d="M1 1l11 9 11-9" stroke="#877a69" stroke-width="2" fill="none"/></svg>info@quor.net</div>
  </div>
  <div class="footer-bar"></div>
  <p class="copyright">© 2017. Quor. All rights reserved</p>
  <div class="social"><span>Connect with our social network</span><i></i><i></i><i></i><i></i><i></i></div>
</footer>

</body>
</html>
```